Flier redesign 2021

The 3 prior year fliers are attached. We want a new design for 2021 -

* DO NOT SIMPLY COPY and change the year.
*All text should be the same, except year is 2021.
*Use different photos. You can find photos on our website maplecrestgardens.org or on our google page.

Requirements
Must have
• MUST be done in photoshop an photoshop file must be provided at the end.
Should not have
• Should not be same design as previous years.

```html
<!DOCTYPE html>
<html lang="en">
<head>
<meta charset="utf-8">
<title>Maplecrest Gardens – 2021 Landscaping Packages</title>
<link href="https://fonts.googleapis.com/css2?family=Cormorant+Garamond:wght@500;600&family=Open+Sans:wght@400;600&display=swap" rel="stylesheet">
<style>
  :root{
    --maroon:#7b1d2e;
    --tan:#b3a872;
    --gold:#dcc763;
    --gold-text:#c9bd80;
    --ink:#4a4a4a;
    --footer:#38393b;
    --page:#ffffff;
    --backdrop:#ece9e2;
  }
  *{box-sizing:border-box;margin:0;padding:0}
  html,body{width:1200px;height:766px;overflow:hidden;background:var(--backdrop)}
  body{font-family:"Open Sans",Arial,sans-serif;color:var(--ink)}

  .flyer{position:absolute;left:313px;top:13px;width:612px;height:791px;background:var(--page);
    transform:scale(0.935);transform-origin:top left;overflow:hidden;box-shadow:0 4px 18px rgba(0,0,0,.18)}

  .hero{position:absolute;left:14px;top:17px;width:584px;height:290px;border-radius:0 14px 0 14px;overflow:hidden;
    background:
      linear-gradient(90deg,#1c130e 0%,#2b1d14 30%,rgba(60,35,20,0) 52%),
      linear-gradient(180deg,#d96a2c 0%,#e2883a 25%,#b94a26 50%,#6a4a2a 72%,#8a7a4e 86%,#6f7a48 100%);}

  .brand-tab{position:absolute;left:40px;top:17px;width:196px;height:146px;background:var(--page);
    border-radius:0 0 20px 20px;display:flex;flex-direction:column;align-items:center;justify-content:center;gap:4px}
  .brand-mark{width:34px;height:34px;border-radius:50%;background:var(--maroon)}
  .brand-name{font-family:"Cormorant Garamond",Georgia,serif;font-weight:600;font-size:26px;line-height:1;color:var(--maroon);text-align:center}

  .hero-year{position:absolute;left:38px;top:172px;font-family:"Cormorant Garamond",Georgia,serif;font-weight:500;font-size:48px;color:var(--gold-text);line-height:1}
  .hero-title{position:absolute;left:39px;top:222px;font-family:"Cormorant Garamond",Georgia,serif;font-weight:600;font-size:29px;color:#fff;line-height:34px;letter-spacing:.5px}

  .scenery{position:absolute;left:0;top:330px;width:612px;height:400px;
    background:linear-gradient(180deg,#ffffff 0%,#f3f3ee 45%,#dfe0cf 80%,#cfd0b6 100%)}

  .card{position:absolute;background:#fff;text-align:center}
  .card-seasonal{left:20px;top:341px;width:184px;height:359px}
  .card-perpetual{left:219px;top:325px;width:184px;height:385px}
  .card-basic{left:415px;top:341px;width:183px;height:359px}

  .card-head{position:absolute;left:0;top:0;width:100%;height:95px;border-radius:6px 6px 0 0;
    clip-path:polygon(0 0,100% 0,100% 72%,50% 100%,0 72%);
    font-family:"Cormorant Garamond",Georgia,serif;font-weight:600;font-size:17px;line-height:20px;color:#fff;padding-top:20px;letter-spacing:.3px}
  .head-maroon{background:var(--maroon)}
  .head-tan{background:var(--tan)}

  .badge{position:absolute;left:231px;top:303px;width:164px;height:24px;background:var(--gold);border-radius:6px 6px 0 0;
    color:#fff;font-size:13px;line-height:24px;text-align:center;letter-spacing:.2px}

  .card-lead{position:absolute;left:0;width:100%;color:var(--maroon);font-size:10.5px;line-height:15px}
  .card-body{position:absolute;left:0;width:100%;text-align:left;font-size:10px;line-height:11px;color:var(--ink)}
  .card-body p{font-size:11px;line-height:15px}
  .features{list-style:none}
  .features li{position:relative;padding-left:9px;margin-bottom:4px}
  .features li::before{content:"";position:absolute;left:1px;top:4px;width:3px;height:3px;border-radius:50%;background:var(--tan)}

  .note{position:absolute;left:0;width:100%;font-size:7px;line-height:9px;color:var(--gold-text)}

  .price{position:absolute;color:#fff;text-align:center}
  .price-maroon{background:var(--maroon)}
  .price-tan{background:var(--tan)}
  .price-label{font-size:8.5px;line-height:10px}
  .price-amount{font-size:17px;font-weight:600;line-height:20px}
  .price-split{display:flex;justify-content:center;padding-top:8px}
  .price-split .term{padding:0 5px;border-left:1px solid rgba(255,255,255,.7)}
  .price-split .term:first-child{border-left:none}

  .footer{position:absolute;left:0;top:740px;width:612px;height:51px;background:var(--footer);display:flex;align-items:center;color:#fff;font-size:11px}
  .footer span{flex:1;text-align:center}
  .footer .divider{flex:0 0 1px;height:24px;background:var(--gold-text)}
</style>
</head>
<body>
<main class="flyer">
  <div class="hero" role="img" aria-label="Photo of a park avenue of trees in red and orange autumn foliage"></div>

  <div class="brand-tab">
    <span class="brand-mark"></span>
    <div class="brand-name">Maplecrest<br>Gardens</div>
  </div>

  <div class="hero-year">2021</div>
  <h1 class="hero-title">LANDXCAPING<br>PACKAGES</h1>

  <div class="scenery" role="img" aria-label="Faded photo of a green cemetery lawn with trees"></div>

  <section class="card card-seasonal">
    <h2 class="card-head head-maroon">SEASONAL<br>CARE</h2>
    <div class="card-lead" style="top:113px">Seasonal landscaping<br>grave care</div>
    <div class="card-body" style="top:160px;padding:0 14px 0 35px">
      <p>Weeding and trimming services on your gravesite approximately every 7 weeks during the growing season: mid-April through mid-October</p>
    </div>
    <div class="note" style="top:286px">Multi-year payment locks in current rates.<br>Valid trough 10/31/21.</div>
    <div class="price price-maroon price-split" style="left:7px;top:315px;width:167px;height:44px">
      <div class="term"><div class="price-label">3 YEARS</div><div class="price-amount">$345</div></div>
      <div class="term"><div class="price-label">2 YEARS</div><div class="price-amount">$230</div></div>
      <div class="term"><div class="price-label">1 YEARS</div><div class="price-amount">$115</div></div>
    </div>
  </section>

  <div class="badge">MOST POPULAR</div>
  <section class="card card-perpetual">
    <h2 class="card-head head-tan">PERPETUAL CARE<br>ENDOWMENT</h2>
    <div class="card-lead" style="top:108px">Landscaping care forever for<br>graves with plantings</div>
    <div class="card-body" style="top:146px;padding:0 14px 0 17px">
      <ul class="features">
        <li>Weeding and trimming services on your gravesite approximately every 7 weeks during the growing season: mid-April through mid-October</li>
        <li>Monument leveling</li>
        <li>Payment ensures grave care forever</li>
        <li>Full bed of boxwood shrubs</li>
        <li>Replacement of shrubs</li>
        <li>Trust certificate</li>
      </ul>
    </div>
    <div class="note" style="top:317px">Call for single payment discount.<br>Valid trough 10/31/21.</div>
    <div class="price price-tan" style="left:16px;top:344px;width:147px;height:43px;padding-top:6px">
      <div class="price-label">12 MONTHLY PAYMENTS OF</div>
      <div class="price-amount" style="color:var(--maroon)">$297</div>
    </div>
  </section>

  <section class="card card-basic">
    <h2 class="card-head head-maroon">BASIC CARE<br>ENDOWMENT</h2>
    <div class="card-lead" style="top:111px;font-size:10px;line-height:13px">Landscaping forever for<br>graves with no plantings</div>
    <div class="card-body" style="top:154px;padding:0 14px 0 20px">
      <ul class="features">
        <li style="margin-bottom:10px">Weeding and trimming services on your gravesite 2 times per year: mid-May and mid-September</li>
        <li style="margin-bottom:6px">Monument leveling</li>
        <li>Payment ensures grave care forever</li>
      </ul>
    </div>
    <div class="note" style="top:286px">Call for single payment discount.<br>Valid trough 10/31/21.</div>
    <div class="price price-maroon" style="left:6px;top:315px;width:169px;height:44px;padding-top:6px">
      <div class="price-label">12 MONTHLY PAYMENTS OF</div>
      <div class="price-amount" style="color:var(--gold)">$239</div>
    </div>
  </section>

  <footer class="footer">
    <span>www.maplecrestgardens.org</span>
    <i class="divider"></i>
    <span>(555) 210-4836</span>
    <i class="divider"></i>
    <span>info@maplecrestgardens.org</span>
  </footer>
</main>
</body>
</html>
```